Cleaning service website design

We need a new nice web design(logo will be the same) for a new cleaning service Company:

Informations about Company and logo you can take from flyers in attachments.

This is a cleaning service Company which have simple rules and we would like to show that(in checklist form) on website:

- What we do and that we're Cleaning Green

- Why us?

- How much(our pricing is simple)

Also we would like to communicate with clients by some nice/big pictures on website and the most important thing is our phone number and short/fast Freestimate.

Also there should be some space for description about our Company.

Generally all information on main page can be short: about us, about service(what we do), last reviews, tips (for example: Tip of the week) and other can be some introduction to subpage where will be more information.

There will be few subpages like: About us, About our service, Photos(Before and after), Reviews , Tips, FAQ, Contact, Looking for a Job? - most of them will be just text so you can project just one example.

```html
<!DOCTYPE html>
<html lang="en">
<head>
<meta charset="utf-8">
<title>Tidy Nest House Cleaning</title>
<link href="https://fonts.googleapis.com/css2?family=Montserrat:wght@400;500;600;700&family=Kaushan+Script&family=Anton&family=Roboto+Condensed:wght@700&family=Libre+Baskerville:ital@1&display=swap" rel="stylesheet">
<style>
:root{
  --blue:#0b58ad;
  --blue-dark:#084a93;
  --green:#6cbf5f;
  --green-line:#8fd083;
  --ink:#2b2b2b;
  --muted:#555;
  --field:#ffffff;
  --panel:#efefef;
  --hero-a:#e8dcc6;
  --hero-b:#c9a77f;
}
*{box-sizing:border-box;margin:0;padding:0}
html,body{width:691px;height:1200px;overflow:hidden;background:#fff}
body{font-family:"Montserrat",Arial,sans-serif;color:var(--ink)}
.page{position:relative;width:691px;height:1200px;overflow:hidden}

/* navigation */
.site-nav{position:absolute;top:0;left:0;width:691px;height:44px;background:var(--blue)}
.site-nav a{position:absolute;top:16px;color:#fff;font-size:8.5px;font-weight:500;text-decoration:none;letter-spacing:.2px}
.brand{position:absolute;left:296px;top:8px;width:100px;height:44px;display:flex;align-items:center;justify-content:center;gap:6px;background:var(--green);border:2px solid #fff;border-radius:8px}
.brand-dot{width:9px;height:9px;border-radius:50%;background:#fff}
.brand-name{color:#fff;font-size:13px;font-weight:700}

/* hero */
.hero{position:absolute;top:44px;left:0;width:691px;height:272px;background:linear-gradient(120deg,var(--hero-a) 0%,#efe6d6 45%,var(--hero-b) 100%)}
.hero-line{position:absolute;color:#111;line-height:1}
.hero-line.script-a{left:128px;top:126px;font-family:"Kaushan Script",cursive;font-size:36px}
.hero-line.block{left:128px;top:170px;font-family:"Anton",sans-serif;font-size:33px;letter-spacing:-.5px}
.hero-line.script-b{left:316px;top:198px;font-family:"Kaushan Script",cursive;font-size:40px}
.slider-arrows{position:absolute;left:560px;top:229px;width:56px;height:32px;background:rgba(255,255,255,.75)}

/* call band */
.call-band{position:absolute;top:316px;left:0;width:691px;height:62px;display:flex;align-items:center;justify-content:center;gap:16px;background:#fff}
.call-lead{font-family:"Kaushan Script",cursive;font-size:25px;color:#1c1c1c}
.call-phone{font-family:"Roboto Condensed",sans-serif;font-weight:700;font-size:27px;color:var(--blue)}

/* checklist band */
.features{position:absolute;top:378px;left:0;width:691px;height:197px;background:var(--green)}
.feature-col{position:absolute;top:0;height:197px;padding-top:13px}
.feature-col + .feature-col{border-left:1px solid var(--green-line)}
.feature-col h2{color:#fff;font-size:12.5px;font-weight:600;letter-spacing:.3px;padding-bottom:10px;border-bottom:2px solid var(--green-line);width:162px}
.feature-col ul{list-style:none;margin-top:15px}
.feature-col li{position:relative;padding-left:17px;color:#fff;font-size:7.6px;line-height:10px;margin-bottom:9px}
.feature-col li svg{position:absolute;left:0;top:1px}

/* intro copy */
.intro{position:absolute;left:75px;top:592px;width:352px}
.eyebrow{font-family:"Libre Baskerville",Georgia,serif;font-style:italic;font-size:13px;color:#444}
.intro h2{color:var(--green);font-size:14px;font-weight:500;letter-spacing:.4px;margin-bottom:10px}
.intro p{font-size:7.7px;line-height:12.3px;color:var(--ink);margin-bottom:12px}
.divider{border:0;border-top:1px solid #e3e3e3;margin:20px 0 24px}
.signature{font-family:"Kaushan Script",cursive;font-size:17px;text-align:right;color:#222;margin-top:14px}

/* estimate form */
.estimate{position:absolute;left:454px;top:597px;width:162px;height:488px;background:var(--panel)}
.estimate h2{height:38px;background:var(--blue);color:#fff;font-size:16px;font-weight:500;letter-spacing:.5px;display:flex;align-items:center;padding-left:15px}
.estimate form{padding:13px 11px 0 10px}
.field{display:block;width:141px;height:25px;margin-bottom:7.5px;background:var(--field);border:1px solid #e2e2e2;font:7.6px "Montserrat",sans-serif;color:#444;padding:0 6px;line-height:23px}
.field.tall{height:62px;line-height:normal;padding-top:7px}
.submit{display:block;width:70px;height:24px;margin-top:3px;background:var(--blue);color:#fff;border:0;font:700 11px "Montserrat",sans-serif;letter-spacing:.5px}

/* footer */
.site-footer{position:absolute;top:1108px;left:0;width:691px;height:52px;background:var(--blue)}
.contact-item{position:absolute;top:13px;display:flex;gap:8px;color:#fff;font-size:7.8px;line-height:11px}
.follow{position:absolute;left:523px;top:19px;display:flex;align-items:center;gap:3px;color:#fff;font-size:8px}
.follow span.round{width:17px;height:17px;border-radius:50%;background:#fff;display:inline-block}
.follow span.label{margin-right:5px}
.footer-links{position:absolute;top:1166px;left:0;width:691px;text-align:center;font-size:7.4px;color:#333}
.footer-links a{color:#333;text-decoration:none;margin:0 3px}
.copyright{position:absolute;top:1183px;left:0;width:691px;text-align:center;font-size:7px;color:#444}
</style>
</head>
<body>
<div class="page">

  <nav class="site-nav">
    <a href="#" style="left:76px">HOME</a>
    <a href="#" style="left:127px">ABOUT US</a>
    <a href="#" style="left:195px">SERVICES</a>
    <a href="#" style="left:258px">TIPS</a>
    <div class="brand"><span class="brand-dot"></span><span class="brand-name">Tidy Nest</span></div>
    <a href="#" style="left:416px">REVIEWS</a>
    <a href="#" style="left:476px">PHOTOS</a>
    <a href="#" style="left:536px">FAQ</a>
    <a href="#" style="left:579px">CONTACT</a>
  </nav>

  <header class="hero" role="img" aria-label="Photo of a smiling family with two children and a golden retriever on a sofa in a bright living room">
    <div class="hero-line script-a">Affordably</div>
    <div class="hero-line block">making your life</div>
    <div class="hero-line script-b">Simpler</div>
    <div class="slider-arrows">
      <svg width="56" height="32" viewBox="0 0 56 32" aria-hidden="true">
        <line x1="28" y1="4" x2="28" y2="28" stroke="#bbb" stroke-width="1"/>
        <polyline points="18,8 12,16 18,24" fill="none" stroke="#333" stroke-width="1.4"/>
        <polyline points="38,8 44,16 38,24" fill="none" stroke="#333" stroke-width="1.4"/>
      </svg>
    </div>
  </header>

  <section class="call-band">
    <span class="call-lead">It's Simple... Call Today</span>
    <span class="call-phone">555-014-2290</span>
  </section>

  <section class="features">
    <div class="feature-col" style="left:0;width:252px;padding-left:76px">
      <h2>WHAT WE DO ?</h2>
      <ul>
        <li><svg width="8" height="7" viewBox="0 0 8 7"><polyline points="1,3.5 3,5.5 7,1" fill="none" stroke="#fff" stroke-width="1.2"/></svg>Thoroughly clean your bathrooms,<br>kitchen, bedrooms and living areas</li>
        <li><svg width="8" height="7" viewBox="0 0 8 7"><polyline points="1,3.5 3,5.5 7,1" fill="none" stroke="#fff" stroke-width="1.2"/></svg>Mop or vacuum your floors</li>
        <li><svg width="8" height="7" viewBox="0 0 8 7"><polyline points="1,3.5 3,5.5 7,1" fill="none" stroke="#fff" stroke-width="1.2"/></svg>Dust surfaces</li>
        <li><svg width="8" height="7" viewBox="0 0 8 7"><polyline points="1,3.5 3,5.5 7,1" fill="none" stroke="#fff" stroke-width="1.2"/></svg>Collect garbage</li>
        <li><svg width="8" height="7" viewBox="0 0 8 7"><polyline points="1,3.5 3,5.5 7,1" fill="none" stroke="#fff" stroke-width="1.2"/></svg>Make beds</li>
      </ul>
    </div>
    <div class="feature-col" style="left:252px;width:188px;padding-left:13px">
      <h2>WHY CHOOSE US?</h2>
      <ul>
        <li><svg width="8" height="7" viewBox="0 0 8 7"><polyline points="1,3.5 3,5.5 7,1" fill="none" stroke="#fff" stroke-width="1.2"/></svg>Owners Present at Every Cleaning</li>
        <li><svg width="8" height="7" viewBox="0 0 8 7"><polyline points="1,3.5 3,5.5 7,1" fill="none" stroke="#fff" stroke-width="1.2"/></svg>Locally Owned &amp; Operated</li>
        <li><svg width="8" height="7" viewBox="0 0 8 7"><polyline points="1,3.5 3,5.5 7,1" fill="none" stroke="#fff" stroke-width="1.2"/></svg>Reliable &amp; Affordable</li>
        <li><svg width="8" height="7" viewBox="0 0 8 7"><polyline points="1,3.5 3,5.5 7,1" fill="none" stroke="#fff" stroke-width="1.2"/></svg>All Supplies Provided</li>
        <li><svg width="8" height="7" viewBox="0 0 8 7"><polyline points="1,3.5 3,5.5 7,1" fill="none" stroke="#fff" stroke-width="1.2"/></svg>Green Cleaning</li>
        <li><svg width="8" height="7" viewBox="0 0 8 7"><polyline points="1,3.5 3,5.5 7,1" fill="none" stroke="#fff" stroke-width="1.2"/></svg>Pet Friendly</li>
        <li><svg width="8" height="7" viewBox="0 0 8 7"><polyline points="1,3.5 3,5.5 7,1" fill="none" stroke="#fff" stroke-width="1.2"/></svg>No Contracts</li>
      </ul>
    </div>
    <div class="feature-col" style="left:440px;width:251px;padding-left:14px">
      <h2>HOW MUCH ?</h2>
      <ul>
        <li><svg width="8" height="7" viewBox="0 0 8 7"><polyline points="1,3.5 3,5.5 7,1" fill="none" stroke="#fff" stroke-width="1.2"/></svg>Locally Owned &amp; Operated</li>
        <li><svg width="8" height="7" viewBox="0 0 8 7"><polyline points="1,3.5 3,5.5 7,1" fill="none" stroke="#fff" stroke-width="1.2"/></svg>Reliable &amp; Affordable</li>
        <li><svg width="8" height="7" viewBox="0 0 8 7"><polyline points="1,3.5 3,5.5 7,1" fill="none" stroke="#fff" stroke-width="1.2"/></svg>All Supplies Provided</li>
        <li><svg width="8" height="7" viewBox="0 0 8 7"><polyline points="1,3.5 3,5.5 7,1" fill="none" stroke="#fff" stroke-width="1.2"/></svg>Green Cleaning</li>
        <li><svg width="8" height="7" viewBox="0 0 8 7"><polyline points="1,3.5 3,5.5 7,1" fill="none" stroke="#fff" stroke-width="1.2"/></svg>Pet Friendly</li>
        <li><svg width="8" height="7" viewBox="0 0 8 7"><polyline points="1,3.5 3,5.5 7,1" fill="none" stroke="#fff" stroke-width="1.2"/></svg>No Contracts</li>
      </ul>
    </div>
  </section>

  <main class="intro">
    <div class="eyebrow">Welcome to</div>
    <h2>TIDY NEST HOUSE CLEANING</h2>
    <p>We are Daniel and Marta Kowalec and we have personally experienced the struggle of finding a reliable and affordable maid service. We understand how busy life can be and cleaning is one of the tasks that falls off the list when you're stretched too thin. We are here to help! Let Tidy Nest take care of the house cleaning so you can focus on the more important things in life.</p>
    <p>Halton, Burlington, Oakville and Milton residents can count on us to make your home sparkle from top to bottom!</p>
    <hr class="divider">
    <div class="eyebrow">Meet</div>
    <h2>MARTA AND DANIEL KOWALEC</h2>
    <p>It's about caring, not just cleaning.</p>
    <p>Having personally experienced the struggles of finding quality maid service for our home, we want to make it simpler for families in the Halton area. Our goal is to provide caring, consistent and reliable house cleaning to every customer we serve.</p>
    <p>We pride ourselves on delivering the best possible customer experience in the region and providing outstanding healthy home cleaning to this important and rapidly growing community.</p>
    <p>We are passionate about making a difference in the community and having Tidy Nest become synonymous with reliable and dependable housekeeping services. With local focus and attention to quality and service we believe the families in the Halton region including Oakville, Burlington and Milton can be confident they are receiving the best and most reliable services in the region.</p>
    <p>We are proud to serve the communities of Oakville, Burlington and Milton.</p>
    <div class="signature">– Marta &amp; Daniel</div>
  </main>

  <aside class="estimate">
    <h2>FREE ESTIMATE</h2>
    <form>
      <div class="field">First Name &amp; Last Name:</div>
      <div class="field">Address line1:</div>
      <div class="field">Address line2:</div>
      <div class="field">City:</div>
      <div class="field">State/Province:</div>
      <div class="field">Zip/Postal Code:</div>
      <div class="field">Phone:</div>
      <div class="field">Email:</div>
      <div class="field tall">How did you hear about us?</div>
      <div class="field tall">Comments:</div>
      <button type="button" class="submit">SUBMIT</button>
    </form>
  </aside>

  <footer class="site-footer">
    <div class="contact-item" style="left:77px">
      <svg width="12" height="16" viewBox="0 0 12 16" aria-hidden="true"><path d="M6 1a5 5 0 0 0-5 5c0 4 5 9 5 9s5-5 5-9a5 5 0 0 0-5-5z" fill="#fff"/><circle cx="6" cy="6" r="2" fill="var(--blue)"/></svg>
      <span>Tidy Nest House<br>Lorem Ipsum amet...</span>
    </div>
    <div class="contact-item" style="left:227px">
      <svg width="11" height="17" viewBox="0 0 11 17" aria-hidden="true"><rect x="1" y="1" width="9" height="15" rx="1.5" fill="none" stroke="#fff" stroke-width="1.5"/><circle cx="5.5" cy="13" r="1" fill="#fff"/></svg>
      <span>Phone:<br>555-014-2290</span>
    </div>
    <div class="contact-item" style="left:355px">
      <svg width="18" height="13" viewBox="0 0 18 13" aria-hidden="true"><rect x="1" y="1" width="16" height="11" fill="none" stroke="#fff" stroke-width="1.5"/><polyline points="1,1 9,7 17,1" fill="none" stroke="#fff" stroke-width="1.5"/></svg>
      <span>Email:<br>hello@tidynest.example</span>
    </div>
    <div class="follow"><span class="label">Follow :</span><span class="round"></span><span class="round"></span><span class="round"></span></div>
  </footer>

  <div class="footer-links">
    <a href="#">Home</a>|<a href="#">About Us</a>|<a href="#">Services</a>|<a href="#">Tips</a>|<a href="#">Reviews</a>|<a href="#">Photos</a>|<a href="#">FAQ</a>|<a href="#">Contact</a>
  </div>
  <div class="copyright">© 2013 Tidy Nest House Cleaning. All Rights Reserved.</div>

</div>
</body>
</html>
```